Ashcombe Ridge Business Cards

We need business card designs for a modern home development, Ashcombe Ridge. We would like to see modern looking designs- clean and simple but striking. I've attached some images of one of the homes so you can see the style of the homes we are putting on the market and perhaps they will inspire your design! I've also attached the logo- both horizontal and vertical. We need to use the logo on the card. I've also attached a sign that has a map of the development. If you can use that and still keep the card nice and clean, great. If not, it's not a problem to leave the map out completely.

```html
<!DOCTYPE html>
<html lang="en">
<head>
<meta charset="utf-8">
<title>Ashcombe Ridge – Business Card</title>
<link rel="stylesheet" href="https://fonts.googleapis.com/css2?family=Open+Sans:wght@600;700;800&family=Roboto+Condensed:ital,wght@0,400;1,400&display=swap">
<style>
  :root {
    --bg-light: #ffffff;
    --bg-edge: #c9d3d3;
    --teal-dark: #17485a;
    --teal-mid: #2a7f90;
    --teal-wave-top: #3ccbd4;
    --teal-wave-bottom: #27929e;
    --ink: #111414;
    --rule: #222;
    --logo-panel: #eef1f1;
    --logo-border: #c3cccc;
  }
  * { margin: 0; padding: 0; box-sizing: border-box; }
  html, body { width: 1200px; height: 720px; overflow: hidden; }
  body { background: var(--bg-edge); }

  .card {
    position: relative;
    width: 1200px;
    height: 720px;
    overflow: hidden;
    background: radial-gradient(ellipse 720px 520px at 420px 250px, var(--bg-light) 0%, #eef1f1 45%, var(--bg-edge) 100%);
    font-family: "Open Sans", Arial, sans-serif;
    color: var(--ink);
  }

  .wave { position: absolute; left: 0; top: 0; width: 1200px; height: 720px; }

  .identity { position: absolute; left: 72px; top: 122px; }
  .identity__name { display: flex; align-items: baseline; white-space: nowrap; }
  .identity__given {
    font-weight: 700;
    font-size: 72px;
    letter-spacing: -0.5px;
    background: linear-gradient(180deg, var(--teal-mid) 0%, var(--teal-dark) 100%);
    -webkit-background-clip: text;
    background-clip: text;
    color: transparent;
  }
  .identity__family {
    font-family: "Roboto Condensed", "Arial Narrow", sans-serif;
    font-weight: 400;
    font-size: 52px;
    margin-left: 16px;
    color: var(--ink);
  }
  .identity__role {
    margin-top: 4px;
    font-weight: 700;
    font-size: 28px;
    letter-spacing: -0.2px;
    color: #1a1d1d;
  }

  .brand-panel {
    position: absolute;
    left: 0; top: 311px;
    width: 464px; height: 137px;
    background: linear-gradient(180deg, #f7f9f9, var(--logo-panel));
    border: 2px solid var(--logo-border);
    display: flex;
    align-items: center;
    gap: 18px;
    padding-left: 28px;
  }
  .brand-panel__square { width: 56px; height: 56px; background: var(--teal-wave-bottom); }
  .brand-panel__name {
    font-weight: 800;
    font-size: 40px;
    letter-spacing: 1px;
    color: var(--ink);
  }

  .divider {
    position: absolute;
    left: 727px; top: 133px;
    width: 1.5px; height: 246px;
    background: var(--rule);
  }

  .contact { position: absolute; left: 735px; top: 174px; list-style: none; }
  .contact__row { display: flex; align-items: baseline; height: 48px; white-space: nowrap; }
  .contact__label { font-weight: 700; font-size: 22px; margin-right: 8px; }
  .contact__value {
    font-family: "Roboto Condensed", "Arial Narrow", sans-serif;
    font-style: italic;
    font-size: 21px;
  }
</style>
</head>
<body>
  <div class="card">
    <svg class="wave" viewBox="0 0 1200 720" aria-hidden="true">
      <defs>
        <linearGradient id="waveTeal" x1="0" y1="0" x2="0" y2="1">
          <stop offset="0" stop-color="var(--teal-wave-top)"/>
          <stop offset="1" stop-color="var(--teal-wave-bottom)"/>
        </linearGradient>
      </defs>
      <path fill="var(--ink)" d="M0 628 C 250 640, 520 560, 760 470 C 930 408, 1080 402, 1200 404 L1200 416 C 1080 420, 940 440, 790 500 C 560 590, 280 670, 0 664 Z"/>
      <path fill="url(#waveTeal)" d="M0 664 C 280 670, 560 590, 790 500 C 940 440, 1080 420, 1200 416 L1200 720 L0 720 Z"/>
    </svg>

    <header class="identity">
      <h1 class="identity__name">
        <span class="identity__given">Danielle R.</span>
        <span class="identity__family">Whitford</span>
      </h1>
      <p class="identity__role">Jr. Developer, Construction Manager</p>
    </header>

    <div class="brand-panel">
      <span class="brand-panel__square"></span>
      <span class="brand-panel__name">ASHCOMBE RIDGE</span>
    </div>

    <div class="divider"></div>

    <ul class="contact">
      <li class="contact__row"><span class="contact__label">Office:</span><span class="contact__value">2740 Larkfield Avenue, Dallas, TX 75206</span></li>
      <li class="contact__row"><span class="contact__label">Phone:</span><span class="contact__value">214.555.0184</span></li>
      <li class="contact__row"><span class="contact__label">Email:</span><span class="contact__value">hello@ashcomberidge.com</span></li>
    </ul>
  </div>
</body>
</html>
```